Hollowmere Capital Stationary Design

We have selected a logo as our winner, we now need a full stationary set to be in the same theme.
Required:
- Letter Head
- Business Card Template
- Custom Envelopes
- A5 Notepad Design (Front cover and content pages. Content pages blank(no lines) but with our branding on them,)
- With Compliments Slip
Updates

Hey All,

We have changed the colour scheme of our logo. Our apologies if anyone has begun designing based off the old scheme. Please see the updated scheme in the brief,

Oliver

Target Market(s)

Target market is experienced property developers and financial institutions.

Industry/Entity Type

Commercial Finance

Font styles to use
Serif

Colors
0054AA
0677BA
7BADD7
CADEEF
E8F1F8
0094D4
00A9DD
6FCCEA
C7EBF8
E9F6FB
00AB8E
00BBA5
67D7C9
C6EFE9
E9F9F6
59FF00
82FF00
B8FF75
E3FFCB
F4FFEA

```html
<!DOCTYPE html>
<html lang="en">
<head>
<meta charset="utf-8">
<title>Hollowmere Capital Stationery Set</title>
<link href="https://fonts.googleapis.com/css2?family=Montserrat:wght@400;500;600;700&family=Tinos:wght@400;700&display=swap" rel="stylesheet">
<style>
:root{
  --brand-blue:#1f3f96;
  --brand-green:#1f8744;
  --paper:#ffffff;
  --backdrop:#e4e5e7;
  --ink-grey:#8a8a8a;
  --ink-dark:#5f5f5f;
}
*{margin:0;padding:0;box-sizing:border-box}
html,body{width:995px;height:1200px;overflow:hidden}
body{background:var(--backdrop);font-family:'Montserrat',Arial,sans-serif;position:relative;color:var(--ink-grey)}
.sheet{position:absolute;background:var(--paper);box-shadow:0 2px 6px rgba(0,0,0,.18)}
.wordmark{display:flex;align-items:center;gap:4px;position:absolute;font-weight:600;letter-spacing:.04em;color:var(--brand-blue);white-space:nowrap;text-transform:uppercase}
.wordmark .mark-square{display:inline-block;background:var(--brand-green)}
.footer-rule{position:absolute;left:0;right:0;display:flex;align-items:center;gap:3px;white-space:nowrap}
.footer-rule::before,.footer-rule::after{content:"";flex:1;height:1px;background:var(--brand-blue)}
.contact-line{display:flex;align-items:center;gap:3px;white-space:nowrap}
.contact-dot{display:inline-block;border-radius:50%;background:var(--brand-green);flex:none}

/* business card front */
.card-front{left:37px;top:51px;width:225px;height:135px;background:var(--brand-blue)}
.card-front .wordmark{color:#fff;font-size:9.5px;left:50%;top:50%;transform:translate(-50%,-50%)}
.card-front .mark-square{width:8px;height:8px}

/* business card back */
.card-back{left:278px;top:51px;width:225px;height:135px}
.card-back .wordmark{font-size:8px;left:50%;top:30px;transform:translateX(-50%)}
.card-back .mark-square{width:7px;height:7px}
.card-person{position:absolute;right:130px;top:76px;text-align:right}
.card-person .person-name{font-size:8.5px;color:var(--brand-blue);font-weight:400;letter-spacing:.02em}
.card-person .person-name b{font-weight:700}
.card-person .person-role{font-size:5px;color:var(--ink-grey)}
.card-divider{position:absolute;left:100px;top:70px;width:1px;height:30px;background:var(--ink-grey)}
.card-contacts{position:absolute;left:104px;top:71px;font-size:6px;line-height:9.5px}
.card-contacts .contact-dot{width:5px;height:5px}
.card-back .footer-rule{top:111px;font-size:4.8px;color:var(--ink-dark)}

/* envelope */
.envelope{left:37px;top:209px;width:466px;height:234px}
.envelope .wordmark{font-size:10px;left:16px;top:22px}
.envelope .mark-square{width:8px;height:8px}
.envelope .footer-rule{top:211px;font-size:8.4px;color:var(--ink-grey)}

/* compliment slip */
.comp-slip{left:38px;top:459px;width:465px;height:213px}
.comp-slip .wordmark{font-size:10px;left:14px;top:28px}
.comp-slip .mark-square{width:8px;height:8px}
.comp-title{position:absolute;right:16px;top:17px;font-family:'Tinos','Times New Roman',serif;font-size:16.5px;color:var(--brand-green);letter-spacing:.01em}
.comp-title strong{color:var(--brand-blue);font-weight:700}
.comp-footer{position:absolute;left:13px;right:0;bottom:8px;display:flex;align-items:flex-end;gap:4px}
.comp-contacts{font-size:7px;line-height:10px;color:var(--ink-dark);flex:none}
.comp-contacts .contact-dot{width:5.5px;height:5.5px}
.comp-rule{flex:1;height:1px;background:var(--brand-blue);margin-bottom:4px}

/* letterhead */
.letterhead{left:519px;top:51px;width:440px;height:621px}
.letterhead .wordmark{font-size:11.5px;left:23px;top:38px}
.letterhead .mark-square{width:9px;height:9px}
.lh-contacts{position:absolute;right:23px;top:31px;font-size:7.3px;line-height:10.6px;text-align:right;color:var(--ink-grey)}
.lh-contacts .contact-line{justify-content:flex-end}
.lh-contacts .contact-dot{width:6px;height:6px;order:2}
.lh-sender{position:absolute;left:26px;top:164px}
.lh-sender .sender-name{font-size:14px;font-weight:700;color:var(--brand-blue);letter-spacing:.02em;margin-bottom:4px}
.lh-sender p{font-size:8.3px;line-height:10px;color:var(--ink-grey);margin-bottom:4px}
.lh-sender p.tight{margin-bottom:0}
.lh-date{position:absolute;right:23px;top:220px;font-size:8.6px;font-weight:600;color:var(--ink-grey)}
.lh-body{position:absolute;left:24px;right:23px;top:250px;font-size:8.1px;line-height:10px;color:var(--ink-grey);text-align:justify}
.lh-body p{margin-bottom:10px}
.lh-body p.joined{margin-bottom:0}
.lh-body p.gap-after{margin-bottom:20px}
.lh-sign-title{position:absolute;right:30px;top:475px;font-size:11.5px;color:var(--ink-dark)}
.lh-signature{position:absolute;left:320px;top:499px;width:82px;height:51px;background:linear-gradient(135deg,#f2f2f2,#e6e6e6);border-radius:3px}
.letterhead .footer-rule{top:586px;font-size:8px;color:var(--ink-grey)}

/* notepad cover */
.notepad-cover{left:141px;top:732px;width:319px;height:425px;background:var(--brand-green);overflow:hidden}
.cover-top{position:absolute;left:0;top:0;width:100%;height:214px;background:var(--brand-blue)}
.cover-tab{position:absolute;left:42px;top:214px;width:235px;height:42px;background:var(--brand-blue)}
.notepad-cover .wordmark{color:#fff;font-size:15px;left:50%;top:214px;transform:translate(-50%,-50%)}
.notepad-cover .mark-square{width:12px;height:12px}
.cover-title{position:absolute;left:0;right:0;top:323px;text-align:center;font-size:33px;font-weight:600;color:#fff;letter-spacing:.01em}
.cover-text{position:absolute;left:40px;right:40px;top:372px;text-align:center;font-size:4.6px;line-height:5.6px;color:#fff}
.cover-text p{margin-bottom:5.5px}

/* notepad content page */
.notepad-page{left:545px;top:732px;width:319px;height:425px}
.notepad-page .wordmark{font-size:7px;left:9px;top:13px}
.notepad-page .mark-square{width:6px;height:6px}
.page-rule{position:absolute;left:0;right:14px;top:415px;height:1px;background:var(--brand-blue)}
.page-number{position:absolute;right:6px;top:412px;font-size:4.5px;font-weight:600;color:var(--brand-blue)}
</style>
</head>
<body>

<section class="sheet card-front" aria-label="Business card front">
  <div class="wordmark"><span class="mark-square"></span>Hollowmere Capital</div>
</section>

<section class="sheet card-back" aria-label="Business card back">
  <div class="wordmark"><span class="mark-square"></span>Hollowmere Capital</div>
  <div class="card-person">
    <div class="person-name">ELENA <b>HART</b></div>
    <div class="person-role">Director &nbsp;/ CEO</div>
  </div>
  <div class="card-divider"></div>
  <div class="card-contacts">
    <div class="contact-line"><span class="contact-dot"></span>555-010-247</div>
    <div class="contact-line"><span class="contact-dot"></span>info@hollowmerecapital.com</div>
    <div class="contact-line"><span class="contact-dot"></span>www.hollowmerecapital.com</div>
  </div>
  <div class="footer-rule">48 Harbour Row, Suite 210, Ashford, TX 0000</div>
</section>

<section class="sheet envelope" aria-label="Envelope">
  <div class="wordmark"><span class="mark-square"></span>Hollowmere Capital</div>
  <div class="footer-rule">48 Harbour Row, Suite 210, Ashford, TX 0000</div>
</section>

<section class="sheet comp-slip" aria-label="With compliments slip">
  <div class="wordmark"><span class="mark-square"></span>Hollowmere Capital</div>
  <div class="comp-title"><strong>WITH</strong> COMPLIMENT</div>
  <div class="comp-footer">
    <div class="comp-contacts">
      <div class="contact-line"><span class="contact-dot"></span>555-010-247</div>
      <div class="contact-line"><span class="contact-dot"></span>info@hollowmerecapital.com</div>
      <div class="contact-line"><span class="contact-dot"></span>www.hollowmerecapital.com</div>
    </div>
    <div class="comp-rule"></div>
  </div>
</section>

<section class="sheet letterhead" aria-label="Letterhead">
  <div class="wordmark"><span class="mark-square"></span>Hollowmere Capital</div>
  <div class="lh-contacts">
    <div class="contact-line">555-010-247<span class="contact-dot"></span></div>
    <div class="contact-line">info@hollowmerecapital.com<span class="contact-dot"></span></div>
    <div class="contact-line">www.hollowmerecapital.com<span class="contact-dot"></span></div>
  </div>
  <div class="lh-sender">
    <div class="sender-name">ELENA HART</div>
    <p>555-014-382</p>
    <p>info@hollowmerecapital.com</p>
    <p class="tight">48 Harbour Row, Suite<br>210 Ashford, TX 0000</p>
  </div>
  <div class="lh-date">12 December, 2023</div>
  <div class="lh-body">
    <p>Lorem ipsum dolor sit amet, consectetuer adipiscing elit, sed diam nonummy nibh euismod tincidunt ut laoreet dolore magna aliquam erat volutpat. Ut wisi enim ad minim veniam, quis nostrud exerci tation ullamcorper suscipit lobortis nisl ut aliquip ex ea commodo consequat. Duis autem vel eum iriure dolor in hendrerit in vulputate velit esse molestie consequat, vel illum dolore eu feugiat nulla facilisis at vero eros et accumsan et iusto odio dignissim qui blandit praesent luptatum zzril delenit augue duis dolore te feugait nulla facilisi.</p>
    <p class="joined">Lorem ipsum dolor sit amet, cons ectetuer adipiscing elit, sed diam nonummy nibh euismod tincidunt ut laoreet dolore magna aliquam erat volutpat. Ut wisi enim ad minim veniam, quis nostrud exerci tation ullamcorper suscipit lobortis nisl ut aliquip ex ea commodo consequat.</p>
    <p class="gap-after">Lorem ipsum dolor sit amet, consectetuer adipiscing elit, sed diam nonummy nibh euismod tincidunt ut laoreet dolore magna aliquam erat</p>
    <p>Lorem ipsum dolor sit amet, cons ectetuer adipiscing elit, sed diam nonummy nibh euismod tincidunt ut laoreet dolore magna aliquam erat volutpat. Ut wisi enim ad minim veniam, quis nostrud exerci tation ullamcorper suscipit lobortis nisl ut aliquip ex ea commodo consequat. Lorem ipsum dolor sit zamet, consectetuer adipiscing elit, sed diam nonummy nibh euismod tincidunt.</p>
  </div>
  <div class="lh-sign-title">Managing Director</div>
  <div class="lh-signature" role="img" aria-label="Handwritten signature of the managing director"></div>
  <div class="footer-rule">48 Harbour Row, Suite 210, Ashford, TX 0000</div>
</section>

<section class="sheet notepad-cover" aria-label="Notepad front cover">
  <div class="cover-top"></div>
  <div class="cover-tab"></div>
  <div class="wordmark"><span class="mark-square"></span>Hollowmere Capital</div>
  <div class="cover-title">Notepad</div>
  <div class="cover-text">
    <p>Lorem ipsum dolor sit amet, consectetuer adipiscing elit, sed diam nonummy nibh euismod tincidunt ut laoreet dolore magna aliquam erat volutpat.</p>
    <p>Ut wisi enim ad minim veniam, quis nostrud exerci tation ullamcorper suscipit lobortis nisl ut aliquip ex ea commodo consequat.</p>
  </div>
</section>

<section class="sheet notepad-page" aria-label="Notepad content page">
  <div class="wordmark"><span class="mark-square"></span>Hollowmere Capital</div>
  <div class="page-rule"></div>
  <div class="page-number">02</div>
</section>

</body>
</html>
```